Corporate Comedy Poster Brochure

I have designed an 10.75 by 15 flat one-sided poster/flyer to mail out for promoting my corporate comedy services. I don't think I did a bad job, but would love to see if someone can create something else for the same purpose, but with an expert hand and eye, as I am not a designer by trade. You should get a sense of it by the PSD example I provided.

FYI: My websites are:
www.paulvantrimm.com/corporate-comedian
www.gigsforstaffnights.com

Target Market(s)

Event Planners, Chambers of Commerce, Human Resources people who might be in charge of the company party, Golf Courses, Banquet Facilities, etc.

Industry/Entity Type

Entertainment Industry

Font styles to use
Sans Serif

Requirements
Must have
• Must have the textual content, headshot, and all logos that are in the PSD I provided.
• 10.75 inches by 15 inches at 300dpi.
• The PSD is on my Stashbox Cloud at :https://files.stashboxcloud.com/file/d/7Kq41mzvtp3WyhaR8cLn2JsXeQ60/view?usp=sharing
• I promise there is no virus or you know who's website to take down, :-)
Nice to have
• 1) Would be nice to have final in Photoshop, as I could then make adjustments easier. I don't know Illustrator well.
• 2) My motif is a poster for a show that is really a flyer promoting the fact that I perform shows. You can stick with this motif, or if you have a better motif, I am open to that.

```html
<!DOCTYPE html>
<html lang="en">
<head>
<meta charset="utf-8">
<title>Paul Vantrimm – Comedy Night @ Your Event</title>
<link rel="stylesheet" href="https://fonts.googleapis.com/css2?family=Anton&family=Oswald:wght@400;600;700&family=Open+Sans:wght@400;700&display=swap">
<style>
:root{
  --red-deep:#5a0508;
  --red:#b3121a;
  --red-bright:#e01f26;
  --gold:#f7c325;
  --yellow:#ffe23a;
  --white:#ffffff;
  --ink:#1b2233;
  --black:#111111;
  --grey:#5c5c5c;
  --strip:#f4f4f4;
}
*{margin:0;padding:0;box-sizing:border-box}
html,body{width:857px;height:1200px;overflow:hidden;background:#ffffff}
.poster{position:relative;width:857px;height:1200px;overflow:hidden;
  background:radial-gradient(ellipse 460px 420px at 300px 300px,#e23a2a 0%,#a8121a 45%,var(--red-deep) 100%);
  font-family:'Oswald',sans-serif;color:var(--white)}
.art{position:absolute}
.masks{left:50px;top:22px;width:505px;height:270px;border-radius:120px 120px 90px 90px;
  background:radial-gradient(ellipse 140px 130px at 25% 45%,rgba(255,229,138,.95),rgba(217,154,22,.85) 70%,rgba(217,154,22,0) 100%),
             radial-gradient(ellipse 140px 130px at 75% 45%,rgba(255,229,138,.95),rgba(217,154,22,.85) 70%,rgba(217,154,22,0) 100%);}
.headshot{left:228px;top:64px;width:150px;height:262px;border-radius:70px 70px 8px 8px;
  background:linear-gradient(180deg,#c9876a 0%,#a8684e 38%,#2b2f3a 58%,#1a1d25 100%)}
.mic{top:240px;width:70px;height:100px;border-radius:35px 35px 10px 10px;
  background:linear-gradient(135deg,#e8e8e8,#8d8d8d 60%,#444)}
.mic-left{left:52px}
.mic-right{left:486px}
.name-arc{position:absolute;left:10px;top:330px;width:590px;height:150px}
.name-arc text{font-family:'Anton',sans-serif;font-size:70px;fill:var(--gold);stroke:#6b2a00;stroke-width:3;paint-order:stroke;letter-spacing:1px}
.marquee{position:absolute;left:120px;top:478px;width:360px;height:158px}
.marquee-title{position:absolute;left:120px;top:492px;width:360px;text-align:center;
  font-family:'Anton',sans-serif;font-size:56px;line-height:64px;color:var(--yellow);text-transform:uppercase}
.event-line{position:absolute;left:0;top:644px;width:600px;text-align:center;
  font-family:'Anton',sans-serif;font-size:60px;line-height:72px;text-transform:uppercase}
.hilarious{position:absolute;left:0;top:724px;width:600px;text-align:center;
  font-family:'Anton',sans-serif;font-size:42px;line-height:46px;color:var(--yellow);text-transform:uppercase}
.subline{position:absolute;left:120px;top:822px;width:360px;text-align:center;
  font-family:'Oswald',sans-serif;font-weight:600;font-size:20px;line-height:25px;text-transform:uppercase}
.quote{position:absolute;left:612px;width:232px;height:200px;background:var(--red-bright);border-radius:50%;
  padding:42px 28px 0 50px;font-family:'Open Sans',sans-serif;font-size:11.5px;line-height:14px;quotes:none}
.quote .mark{position:absolute;left:20px;top:30px;font-family:'Anton',sans-serif;font-size:38px;line-height:38px}
.quote cite{display:block;margin-top:6px;font-style:normal;font-weight:700}
.quote-one{top:18px}
.quote-two{top:230px}
.services{position:absolute;left:640px;top:448px;list-style:none;font-family:'Oswald',sans-serif;font-weight:700;
  font-size:21px;line-height:29px;color:var(--yellow);text-transform:uppercase}
.partner-strip{position:absolute;left:0;top:1040px;width:605px;height:100px;background:var(--strip);
  display:flex;align-items:center;justify-content:space-around;padding:0 30px}
.partner{font-family:'Oswald',sans-serif;font-weight:700;font-size:22px;color:var(--ink)}
.partner-badge{width:64px;height:64px;border-radius:50%;background:#2f6fb3}
.clients{position:absolute;left:605px;top:636px;width:240px;height:494px;background:var(--white);
  border:2px solid #e3e3e3;padding:16px 14px;color:var(--ink);display:flex;flex-direction:column}
.clients h2{font-family:'Oswald',sans-serif;font-weight:700;font-size:21px;line-height:24px;color:var(--red);text-align:center;text-transform:uppercase;margin-bottom:18px}
.client-grid{display:grid;grid-template-columns:1fr 1fr;row-gap:30px;column-gap:8px;align-items:center}
.client{font-family:'Oswald',sans-serif;font-weight:600;font-size:15px;color:var(--ink);display:flex;align-items:center;gap:5px}
.client .dot{width:10px;height:10px;background:var(--red);border-radius:50%;flex:none}
.clients p{margin-top:auto;font-family:'Open Sans',sans-serif;font-size:11px;line-height:14px;color:var(--grey);text-align:center}
.footer{position:absolute;left:0;top:1140px;width:857px;height:60px;background:var(--black);display:flex;align-items:center;
  justify-content:space-around;font-family:'Open Sans',sans-serif;font-size:14px}
.footer span{display:flex;align-items:center;gap:8px}
.footer svg{flex:none}
</style>
</head>
<body>
<main class="poster">
  <div class="art masks" role="img" aria-label="Pair of gold comedy and tragedy theatre masks"></div>
  <div class="art headshot" role="img" aria-label="Headshot of the comedian in a dark suit"></div>
  <div class="art mic mic-left" role="img" aria-label="Vintage silver microphone"></div>
  <div class="art mic mic-right" role="img" aria-label="Vintage silver microphone"></div>

  <svg class="name-arc" viewBox="0 0 590 150" aria-label="Paul Vantrimm">
    <defs><path id="nameCurve" d="M40 140 Q295 30 550 140"/></defs>
    <text text-anchor="middle"><textPath href="#nameCurve" startOffset="50%">Paul Vantrimm</textPath></text>
  </svg>

  <svg class="marquee" viewBox="0 0 360 158" aria-hidden="true">
    <rect x="4" y="4" width="352" height="150" rx="18" fill="#c4141c" stroke="#f7c325" stroke-width="6"/>
    <g fill="#fff6b0">
      <circle cx="28" cy="19" r="4.5"/><circle cx="66" cy="19" r="4.5"/><circle cx="104" cy="19" r="4.5"/><circle cx="142" cy="19" r="4.5"/><circle cx="180" cy="19" r="4.5"/><circle cx="218" cy="19" r="4.5"/><circle cx="256" cy="19" r="4.5"/><circle cx="294" cy="19" r="4.5"/><circle cx="332" cy="19" r="4.5"/>
      <circle cx="28" cy="139" r="4.5"/><circle cx="66" cy="139" r="4.5"/><circle cx="104" cy="139" r="4.5"/><circle cx="142" cy="139" r="4.5"/><circle cx="180" cy="139" r="4.5"/><circle cx="218" cy="139" r="4.5"/><circle cx="256" cy="139" r="4.5"/><circle cx="294" cy="139" r="4.5"/><circle cx="332" cy="139" r="4.5"/>
      <circle cx="18" cy="60" r="4.5"/><circle cx="18" cy="99" r="4.5"/><circle cx="342" cy="60" r="4.5"/><circle cx="342" cy="99" r="4.5"/>
    </g>
  </svg>
  <h1 class="marquee-title">Comedy<br>Night</h1>

  <p class="event-line">@ Your Event</p>
  <p class="hilarious">Hilarious<br>Entertainment</p>
  <p class="subline">For any corporate,<br>club or dinner event!</p>

  <blockquote class="quote quote-one">
    <span class="mark">&ldquo;</span>
    Your show was AMAZING! People are telling us days later how much fun they had and how glad they were you came.
    <cite>Steadfast Insurance</cite>
  </blockquote>
  <blockquote class="quote quote-two">
    <span class="mark">&ldquo;</span>
    What I can tell you is we had a great evening. The laughs never stopped all night.
    <cite>Ridgefield Country Club</cite>
  </blockquote>

  <ul class="services">
    <li>Holiday Parties</li>
    <li>Awards Banquets</li>
    <li>Dinner Shows</li>
    <li>Country Clubs</li>
    <li>Community Shows</li>
    <li>Fundraisers</li>
  </ul>

  <div class="partner-strip">
    <span class="partner">Laughwave</span>
    <span class="partner-badge" role="img" aria-label="Partner badge"></span>
    <span class="partner">Orbit Radio</span>
  </div>

  <section class="clients">
    <h2>Some previous<br>satisfied clients</h2>
    <div class="client-grid">
      <span class="client"><span class="dot"></span>Fieldstone</span>
      <span class="client">Altura Air</span>
      <span class="client">Harvest Co</span>
      <span class="client">Steadfast</span>
      <span class="client"><span class="dot"></span>Buildwell</span>
      <span class="client">Signalwave</span>
      <span class="client">Covera</span>
      <span class="client">Maplewood Grill</span>
      <span class="client">Regal Greens</span>
      <span class="client">FreshMart</span>
    </div>
    <p>And many other companies, country clubs and associations both large and small</p>
  </section>

  <footer class="footer">
    <span>For More Information</span>
    <span><svg width="18" height="18" viewBox="0 0 24 24"><path fill="#fff" d="M6.6 10.8a15 15 0 006.6 6.6l2.2-2.2a1 1 0 011-.25 11.4 11.4 0 003.6.57 1 1 0 011 1V20a1 1 0 01-1 1A17 17 0 013 4a1 1 0 011-1h3.5a1 1 0 011 1c0 1.25.2 2.45.57 3.6a1 1 0 01-.25 1z"/></svg>888-555-0142</span>
    <span><svg width="18" height="18" viewBox="0 0 24 24"><rect x="2" y="5" width="20" height="14" rx="2" fill="#fff"/><path d="M3 6l9 7 9-7" stroke="#111" stroke-width="2" fill="none"/></svg>comedian@paulvantrimm.com</span>
    <span><svg width="18" height="18" viewBox="0 0 24 24"><circle cx="12" cy="12" r="9" stroke="#fff" stroke-width="2" fill="none"/><path d="M3 12h18M12 3c3 3 3 15 0 18M12 3c-3 3-3 15 0 18" stroke="#fff" stroke-width="1.6" fill="none"/></svg>www.paulvantrimm.com</span>
  </footer>
</main>
</body>
</html>
```